Lantern Holdings Business Card

We are looking to design new business cards for our company. We have two office locations and would like to have both full addresses on the card. Each address needs two lines for the building name and street address and a line or two for the city, state and zip code. There should be a place for 2-3 phone numbers. The addresses and phone numbers are at the bottom of this description. We also need a place to put our company website and one email address. Our logo is attached.
We would like the card to be two sided. The back of the card should have a blue background with some part of our logo design on it. We would like the full logo on the front of the card as well. The front of the card should have a white background with the blue logo. We are open to listing our addresses on the front or the back of the card. The person who designed our logo gave us an excellent business card idea that we really liked. I have attached a picture of his business card idea so that we can build off of it.
Addresses:
The Marlow Exchange
2214 47th Street NW
Washington, DC 20419
Osprey Harbor Tower
815 Tamsin Boulevard #2207
Miami, FL 33987
Phone Numbers: (202) 555-0148
(202) 555-0193
Website: www.lanternholdings-example.com

```html
<!DOCTYPE html>
<html lang="en">
<head>
<meta charset="utf-8">
<title>Lantern Holdings Business Card</title>
<link rel="stylesheet" href="https://fonts.googleapis.com/css2?family=PT+Sans+Narrow:wght@400;700&display=swap">
<style>
  :root {
    --backdrop: #808184;
    --paper: #ffffff;
    --navy: #2b3079;
    --panel-blue: #0d56a7;
    --rule: #9a9cc8;
    --ink-light: #ffffff;
  }
  * { margin: 0; padding: 0; box-sizing: border-box; }
  html, body {
    width: 982px;
    height: 1200px;
    overflow: hidden;
  }
  body {
    background: var(--backdrop);
    position: relative;
    font-family: "PT Sans Narrow", "Arial Narrow", sans-serif;
  }
  .card {
    position: absolute;
    overflow: hidden;
    border: 1px solid #5e5f63;
  }
  .card-front {
    left: 31px; top: 41px;
    width: 915px; height: 528px;
    background: var(--paper);
  }
  .wordmark {
    position: absolute;
    left: 127px; top: 183px;
    display: flex;
    align-items: center;
    gap: 20px;
  }
  .wordmark-square {
    width: 126px; height: 126px;
    background: var(--navy);
    border-radius: 14px;
  }
  .wordmark-name {
    color: var(--navy);
    font-weight: 400;
    font-size: 66px;
    line-height: 62px;
    letter-spacing: 4px;
    text-transform: uppercase;
  }
  .wordmark-name .line { display: block; }
  .wordmark-name .line-spaced { letter-spacing: 19px; }
  .web-band {
    position: absolute;
    left: 0; bottom: 0;
    width: 100%; height: 69px;
    background: var(--navy);
    color: var(--ink-light);
    font-size: 21px;
    line-height: 69px;
    text-align: center;
  }
  .card-back {
    left: 34px; top: 616px;
    width: 914px; height: 528px;
    background: var(--navy);
  }
  .brand-panel {
    position: absolute;
    left: 0; top: 0;
    width: 417px; height: 100%;
    background: var(--panel-blue);
    border-top-right-radius: 44px;
  }
  .office {
    position: absolute;
    left: 520px;
    padding-left: 41px;
    color: var(--ink-light);
    font-size: 22px;
    line-height: 29px;
  }
  .office::before {
    content: "";
    position: absolute;
    left: 0; top: 2px;
    width: 7px; height: 82px;
    background: var(--rule);
  }
  .office-dc { top: 102px; }
  .office-miami { top: 226px; }
  .phones {
    position: absolute;
    left: 513px; top: 354px;
    color: var(--ink-light);
    font-size: 40px;
    line-height: 50px;
    list-style: none;
  }
</style>
</head>
<body>
  <section class="card card-front" aria-label="Card front">
    <div class="wordmark">
      <div class="wordmark-square"></div>
      <div class="wordmark-name">
        <span class="line">Lantern</span>
        <span class="line line-spaced">Holdings</span>
      </div>
    </div>
    <div class="web-band">www.lanternholdings-example.com</div>
  </section>

  <section class="card card-back" aria-label="Card back">
    <div class="brand-panel"></div>
    <address class="office office-dc" style="font-style:normal">
      The Marlow Exchange<br>
      2214 47th Street NW<br>
      Washington, DC 20419
    </address>
    <address class="office office-miami" style="font-style:normal">
      Osprey Harbor Tower<br>
      815 Tamsin Boulevard #2207<br>
      Miami, FL 33987
    </address>
    <ul class="phones">
      <li>(202) 555-0148</li>
      <li>(202) 555-0193</li>
    </ul>
  </section>
</body>
</html>
```